Downloadable PDF "Brochure?"

We have a Free download we will provide in exchange for an email address on our new Trailmark website. The website at www.venturetrailmark-example.com is in development and will look nothing like what it currently does, but you can go there and get a sense of what Trailmark is from the text on the website. (see the attached image 'site design' for the new redesigned website for aesthetics).

We are looking for a nice design for the document, that will represent the mostly text document well. We are not actually looking to print these at a printer so they don't have to be print ready. I went ahead and included the logo and colors and fonts file again just for reference.

Target Market(s)

Business Owners / Decision Makers

Requirements
Must have
• See attached document 'trailmark freebie' for text to be utilized in the finished deliverable.
• See the attached image 'Site Design' for the website aesthetic.

```html
<!DOCTYPE html>
<html lang="en">
<head>
<meta charset="utf-8">
<title>Trailmark – 10 Questions To Choose The Best Technology Advisor</title>
<link href="https://fonts.googleapis.com/css2?family=Marcellus+SC&family=Open+Sans:wght@400;600&display=swap" rel="stylesheet">
<style>
  :root {
    --slate: #3c4852;
    --orange: #d9783a;
    --paper: #ffffff;
    --backdrop: #d8d9da;
    --ink: #4a525a;
    --muted: #8a9096;
    --rule: #d5d8db;
  }
  * { box-sizing: border-box; margin: 0; padding: 0; }
  html, body { width: 880px; height: 1200px; overflow: hidden; }
  body { background: var(--backdrop); font-family: "Open Sans", sans-serif; color: var(--ink); position: relative; }

  .page { position: absolute; width: 385px; height: 540px; background: var(--paper); box-shadow: 0 2px 8px rgba(0,0,0,.18); overflow: hidden; }
  .page--cover { left: 40px; top: 40px; }
  .page--questions-a { left: 455px; top: 40px; }
  .page--questions-b { left: 40px; top: 620px; }
  .page--questions-c { left: 455px; top: 620px; }

  .wordmark { font-family: "Open Sans", sans-serif; font-weight: 600; font-size: 17px; letter-spacing: 2px; text-transform: uppercase; color: var(--slate); line-height: 1; }

  /* cover */
  .cover__wordmark { position: absolute; right: 28px; top: 48px; }
  .cover__photo { position: absolute; left: 0; top: 110px; width: 385px; height: 320px;
    background: radial-gradient(ellipse at 35% 45%, #eef1f3 0%, #a9b3bb 40%, #56626c 100%); }
  .cover__panel { position: absolute; left: 190px; top: 200px; width: 195px; height: 150px; background: var(--slate); padding: 22px 18px; border-left: 4px solid var(--orange); }
  .cover__title { font-family: "Marcellus SC", serif; font-size: 18px; line-height: 1.25; color: #fff; font-weight: 400; }
  .cover__subtitle { font-size: 7.5px; line-height: 1.5; color: #d5dadf; margin-top: 10px; }
  .cover__accent { position: absolute; left: 0; top: 430px; width: 190px; height: 10px; background: var(--orange); }
  .page__url { position: absolute; right: 20px; bottom: 16px; font-size: 7px; color: var(--muted); letter-spacing: .5px; }

  /* inner pages */
  .page__stripe { position: absolute; left: 0; top: 0; width: 14px; height: 100%; background: var(--slate); }
  .page__stripe::before { content: ""; position: absolute; left: 0; top: 28px; width: 14px; height: 56px; background: var(--orange); }
  .page__footer-rule { position: absolute; left: 14px; right: 0; bottom: 36px; height: 1px; background: var(--rule); }
  .page__body { position: absolute; left: 34px; right: 22px; top: 28px; }
  .page__title { font-family: "Marcellus SC", serif; font-size: 18px; line-height: 1.2; color: var(--slate); font-weight: 400; }
  .page__title-rule { width: 90px; height: 3px; background: var(--orange); margin: 10px 0 12px; }
  .intro { font-size: 7px; line-height: 1.6; margin-bottom: 12px; }
  .question { margin-bottom: 13px; }
  .question__heading { font-size: 7.5px; font-weight: 600; color: var(--orange); text-transform: uppercase; letter-spacing: .4px; margin-bottom: 4px; line-height: 1.4; }
  .question__text { font-size: 7px; line-height: 1.6; }

  /* contact */
  .contact { position: absolute; left: 34px; right: 22px; top: 300px; height: 200px; background: var(--slate); border-left: 6px solid var(--orange); padding: 18px 20px; color: #e6e9ec; }
  .contact__heading { font-family: "Marcellus SC", serif; font-size: 14px; color: #fff; margin-bottom: 12px; font-weight: 400; }
  .contact__line { display: flex; align-items: center; gap: 8px; font-size: 7.5px; margin-bottom: 9px; line-height: 1.4; }
  .contact__line svg { width: 11px; height: 11px; flex: none; }
  .contact__wordmark { position: absolute; right: 20px; bottom: 18px; color: #fff; font-size: 14px; }
</style>
</head>
<body>

<section class="page page--cover">
  <div class="wordmark cover__wordmark">Trailmark</div>
  <div class="cover__photo" role="img" aria-label="Photo of a businessman standing in a keyhole-shaped opening looking out over a city skyline"></div>
  <div class="cover__panel">
    <h1 class="cover__title">Technology Advisors That “Get” Business</h1>
    <p class="cover__subtitle">We help you leverage technology to create a competitive advantage</p>
  </div>
  <div class="cover__accent"></div>
  <div class="page__url">www.venturetrailmark-example.com</div>
</section>

<section class="page page--questions-a">
  <div class="page__stripe"></div>
  <div class="page__body">
    <h2 class="page__title">10 Questions To Choose<br>The Best Technology Advisor</h2>
    <div class="page__title-rule"></div>
    <p class="intro">Choosing a technology advisor is a big decision. The right partner understands your goals, your people and your budget, and helps you turn technology into a real advantage. Use these questions to compare advisors with confidence.</p>
    <div class="question">
      <h3 class="question__heading">What is the advisor's experience in your industry?</h3>
      <p class="question__text">Look for a partner who has solved problems like yours before and can point to real results for similar businesses. Ask for examples of projects, the size of the companies involved and what changed after the work was done.</p>
    </div>
    <div class="question">
      <h3 class="question__heading">How do they align technology with business goals?</h3>
      <p class="question__text">Good advisors start with your strategy, not with products. They should ask about growth plans, customers and staff before they talk about hardware, software or licences.</p>
    </div>
    <div class="question">
      <h3 class="question__heading">Do they offer a clear roadmap and budget?</h3>
      <p class="question__text">A written plan with costs and milestones keeps everyone accountable and removes surprises from the year ahead. It also helps you plan spending well in advance.</p>
    </div>
    <div class="question">
      <h3 class="question__heading">How will they keep your data secure?</h3>
      <p class="question__text">Ask how they protect systems, back up files, train staff and respond when something goes wrong. A clear recovery plan is a sign of a mature advisor.</p>
    </div>
  </div>
  <div class="page__footer-rule"></div>
  <div class="page__url">www.venturetrailmark-example.com</div>
</section>

<section class="page page--questions-b">
  <div class="page__stripe"></div>
  <div class="page__body">
    <div class="question">
      <h3 class="question__heading">What is included in the monthly fee?</h3>
      <p class="question__text">Clear pricing matters. Make sure support hours, updates, monitoring and planning meetings are listed so you know exactly what you are paying for and where extra charges may apply.</p>
    </div>
    <div class="question">
      <h3 class="question__heading">Who will be your main point of contact?</h3>
      <p class="question__text">One named person who knows your business saves time and builds trust over the long term. Ask how quickly they respond and who steps in when they are away.</p>
    </div>
    <div class="question">
      <h3 class="question__heading">How do they measure success?</h3>
      <p class="question__text">Agree on simple measures such as uptime, response times and staff satisfaction, and review them together every quarter. Reports should be short, clear and focused on outcomes.</p>
    </div>
    <div class="question">
      <h3 class="question__heading">Can they grow with your company?</h3>
      <p class="question__text">Your advisor should scale as you add people, offices and tools, without forcing you to start over. Ask how they have supported other clients through growth and change.</p>
    </div>
    <div class="question">
      <h3 class="question__heading">How do they stay current?</h3>
      <p class="question__text">Technology moves quickly. A strong partner invests in training and shares new ideas that could save you time or money.</p>
    </div>
  </div>
  <div class="page__footer-rule"></div>
  <div class="page__url">www.venturetrailmark-example.com</div>
</section>

<section class="page page--questions-c">
  <div class="page__stripe"></div>
  <div class="page__body">
    <div class="question">
      <h3 class="question__heading">Do they explain things in plain language?</h3>
      <p class="question__text">Technology should feel understandable. Choose a partner who explains options clearly, avoids jargon and helps your team make confident decisions.</p>
    </div>
    <div class="question">
      <h3 class="question__heading">Can they share references from current clients?</h3>
      <p class="question__text">Speak with a few clients directly. Their stories about service, communication and results will tell you more than any sales presentation.</p>
    </div>
    <div class="question">
      <h3 class="question__heading">Ready to take the next step?</h3>
      <p class="question__text">We would be glad to answer these questions for you. Reach out today to book a short conversation about your goals.</p>
    </div>
  </div>
  <div class="contact">
    <h3 class="contact__heading">Contact Us</h3>
    <div class="contact__line">
      <svg viewBox="0 0 12 12"><path d="M3 1h2l1 3-1.5 1a6 6 0 0 0 2.5 2.5L8 6l3 1v2a1 1 0 0 1-1 1A9 9 0 0 1 2 2a1 1 0 0 1 1-1z" fill="#d9783a"/></svg>
      <span>(555) 012-3456</span>
    </div>
    <div class="contact__line">
      <svg viewBox="0 0 12 12"><rect x="1" y="2.5" width="10" height="7" fill="none" stroke="#d9783a" stroke-width="1.2"/><path d="M1 3l5 4 5-4" fill="none" stroke="#d9783a" stroke-width="1.2"/></svg>
      <span>hello@venturetrailmark-example.com</span>
    </div>
    <div class="contact__line">
      <svg viewBox="0 0 12 12"><circle cx="6" cy="6" r="4.8" fill="none" stroke="#d9783a" stroke-width="1.2"/><path d="M1.2 6h9.6M6 1.2c2 2.5 2 7.1 0 9.6M6 1.2c-2 2.5-2 7.1 0 9.6" fill="none" stroke="#d9783a" stroke-width="1"/></svg>
      <span>www.venturetrailmark-example.com</span>
    </div>
    <div class="contact__line">
      <svg viewBox="0 0 12 12"><path d="M6 11S2 7 2 4.5a4 4 0 0 1 8 0C10 7 6 11 6 11z" fill="#d9783a"/><circle cx="6" cy="4.5" r="1.4" fill="#3c4852"/></svg>
      <span>100 Example Street, Suite 200<br>Springfield, ST 00000</span>
    </div>
    <div class="wordmark contact__wordmark">Trailmark</div>
  </div>
</section>

</body>
</html>
```